TEK Logistics - Banner 2.5' x 8' for 20+ locations

Need a banner designed that will pop. This banner will be displayed at over 20 of our transportation facilities. Goal is for the banner to grab the attention of employees, contractors and clients and help reinforce our mission and core values. Designed needs to include TEK Logo, our core values and mission statement. Red and Black are the main company colors and we need to stay within that theme and color pallet. Attached is a previous version that was too basic and boring. Willing to consider a design that excludes the mission statement.

Gathering more feedback

```html
<!DOCTYPE html>
<html lang="en">
<head>
<meta charset="utf-8">
<title>TEK Logistics – Core Values Banner</title>
<link rel="stylesheet" href="https://fonts.googleapis.com/css2?family=Montserrat:wght@300;400;700;800&display=swap">
<style>
  :root {
    --brand-red: #d2231c;
    --brand-black: #222222;
    --paper: #ffffff;
    --stage: #e6e6e6;
    --on-red: #ffffff;
  }
  * { margin: 0; padding: 0; box-sizing: border-box; }
  html, body {
    width: 1200px; height: 1049px; overflow: hidden;
    background: var(--stage);
    font-family: "Montserrat", sans-serif;
  }
  .banner {
    position: absolute; left: 40px; top: 350px;
    width: 1120px; height: 349px;
    background: var(--paper);
    overflow: hidden;
    box-shadow: 0 6px 18px rgba(0,0,0,.18);
  }
  .brand-name {
    position: absolute; left: 52px; top: 92px; width: 270px;
    color: var(--brand-red);
    font-weight: 800; font-size: 46px; line-height: 1.05;
    text-align: center;
  }
  .web-button {
    position: absolute; left: 52px; top: 276px;
    width: 270px; height: 36px;
    background: var(--brand-red); border-radius: 4px;
    box-shadow: 0 2px 0 var(--brand-black);
    color: var(--on-red);
    font-weight: 700; font-size: 14px; letter-spacing: 1.6px;
    display: flex; align-items: center; justify-content: center;
  }
  .value { position: absolute; line-height: 1; white-space: nowrap; }
  .lead { font-weight: 400; font-size: 18px; color: var(--brand-black); }
  .lead.red { color: var(--brand-red); }
  .key { font-weight: 800; font-size: 28px; color: var(--brand-red); letter-spacing: -0.3px; }
  .key.black { color: var(--brand-black); }
  .key.huge { font-size: 60px; letter-spacing: -1px; }
  .key.wow { font-size: 30px; letter-spacing: -1px; }
  .mission {
    position: absolute; left: 817px; top: 38px;
    width: 280px; height: 280px;
    border-radius: 50%;
    background: var(--brand-red);
    display: flex; align-items: center; justify-content: center;
  }
  .mission-text {
    width: 230px; text-align: center;
    color: var(--on-red);
    font-size: 17px; line-height: 24.6px; font-weight: 300;
  }
  .mission-text strong { font-weight: 700; }
</style>
</head>
<body>
  <main class="banner">
    <div class="brand-name">TEK<br>Logistics</div>
    <div class="web-button">www.teklogistics-hub.com</div>

    <span class="value lead" style="left:345px;top:30px;">Do the</span>
    <span class="value key huge" style="left:386px;top:28px;">right</span>
    <span class="value key black" style="left:555px;top:36px;">things</span>
    <span class="value lead red" style="left:662px;top:44px;">for the</span>
    <span class="value key black" style="left:555px;top:64px;">reasons</span>

    <span class="value lead" style="left:408px;top:114px;">Pursue</span>
    <span class="value key" style="left:484px;top:109px;">growth</span>
    <span class="value lead" style="left:605px;top:120px;">and</span>
    <span class="value key" style="left:527px;top:138px;">development</span>

    <span class="value lead" style="left:338px;top:162px;">Build a</span>
    <span class="value key" style="left:367px;top:173px;">positive team</span>
    <span class="value lead" style="left:500px;top:204px;">atmosphere</span>

    <span class="value lead" style="left:419px;top:245px;">Deliver</span>
    <span class="value key wow" style="left:491px;top:235px;">WOW</span>
    <span class="value lead" style="left:586px;top:237px;">through service</span>

    <span class="value lead" style="left:549px;top:274px;">Do everything</span>
    <span class="value key" style="left:609px;top:296px;">Safely</span>

    <span class="value lead" style="left:368px;top:299px;">Have</span>
    <span class="value key" style="left:423px;top:291px;">Fun</span>

    <div class="mission">
      <p class="mission-text">
        Provide <strong>the best customer experience</strong> while creating an
        <strong>environment of growth and opportunity</strong> for our
        <strong>customers, employees,</strong> and <strong>service providers.</strong>
      </p>
    </div>
  </main>
</body>
</html>
```